Designing a billboard

Should have
Corwell & Pine, LLC
Ph: 512-647-3918
Auto Accidents / Personal Injury
Family Law
Criminal Defense
Real Estate
Free Consultation

Target Market(s)

Legal

Industry/Entity Type

Legal

Font styles to use
Serif
Sans Serif

Requirements
Must have
• Designing a billboard

Should have
Corwell & Pine, LLC
Ph: 512-647-3918
Family Law
Criminal Defense
Real Estate
Free Consultation
Nice to have
• Nice to have info above
Should not have
• None

```html
<!DOCTYPE html>
<html lang="en">
<head>
<meta charset="utf-8">
<title>Corwell &amp; Pine, LLC — Billboard</title>
<link rel="stylesheet" href="https://fonts.googleapis.com/css2?family=Playfair+Display:wght@500&family=Montserrat:wght@600&display=swap">
<style>
  :root {
    --page-bg: #eceae8;
    --board-dark: #120e0d;
    --board-mid: #1d1614;
    --title-white: #ffffff;
    --text-white: #f7f5f3;
    --accent-tan: #c49a6c;
    --gavel-warm: #5a3322;
    --gavel-glow: #8a5a3c;
  }
  * { margin: 0; padding: 0; box-sizing: border-box; }
  html, body {
    width: 1200px;
    height: 1181px;
    overflow: hidden;
    background: var(--page-bg);
  }
  .canvas {
    position: relative;
    width: 1200px;
    height: 1181px;
  }
  .billboard {
    position: absolute;
    left: 0;
    top: 399px;
    width: 1200px;
    height: 383px;
    background: linear-gradient(90deg, var(--board-dark) 0%, var(--board-mid) 55%, var(--board-dark) 100%);
    overflow: hidden;
  }
  .firm-name {
    position: absolute;
    left: 56px;
    top: 34px;
    font-family: "Playfair Display", serif;
    font-weight: 500;
    font-size: 66px;
    line-height: 1;
    color: var(--title-white);
    text-transform: uppercase;
    white-space: nowrap;
  }
  .practice-list {
    position: absolute;
    left: 56px;
    top: 128px;
    list-style: none;
    font-family: "Montserrat", sans-serif;
    font-weight: 600;
    font-size: 25px;
    line-height: 32.4px;
    letter-spacing: 0.12em;
    color: var(--text-white);
    text-transform: uppercase;
  }
  .practice-list li {
    display: flex;
    align-items: center;
    white-space: nowrap;
  }
  .practice-list li::before {
    content: "";
    width: 11px;
    height: 11px;
    border-radius: 50%;
    background: var(--text-white);
    margin-right: 9px;
    flex: none;
  }
  .phone {
    position: absolute;
    left: 52px;
    top: 298px;
    font-family: "Montserrat", sans-serif;
    font-weight: 600;
    font-size: 64px;
    line-height: 1;
    letter-spacing: 0.08em;
    color: var(--accent-tan);
    white-space: nowrap;
  }
  .gavel-art {
    position: absolute;
    left: 840px;
    top: 20px;
    width: 345px;
    height: 350px;
    border-radius: 8px;
    background:
      radial-gradient(ellipse at 45% 40%, var(--gavel-glow) 0%, var(--gavel-warm) 30%, rgba(40, 22, 15, 0.6) 60%, rgba(18, 14, 13, 0) 80%);
  }
</style>
</head>
<body>
  <main class="canvas">
    <section class="billboard">
      <h1 class="firm-name">Corwell &amp; Pine, LLC</h1>
      <ul class="practice-list">
        <li>Auto Accidents / Personal Injury</li>
        <li>Family Law</li>
        <li>Criminal Defense</li>
        <li>Real Estate</li>
        <li>Free Consultation</li>
      </ul>
      <p class="phone">PH: 512-647-3918</p>
      <div class="gavel-art" role="img" aria-label="Wooden judge's gavel with gold bands striking its sound block in a warm glowing light"></div>
    </section>
  </main>
</body>
</html>
```